Postcard Designs - Brantley and Corvane

We are a locally owned, family operated pool service and repair company. The postcards we want to have designed is to co-market with two different companies (Brantley and Corvane) . Both companies manufacture variable speed pumps. We are looking for customers who want to upgrade their systems to save $ on energy costs.

Both postcards are basically the same (and can use the same image rather than 2 different like I have in the Word doc). We just need to modify the text and company logo.

Postcard Specs

Full Bleed Size (starting document size)
8.64" x 5.59"
219 x 142 mm
2592 x 1677 pixels
* Finished artwork should use the full bleed dimensions for best results.
Document Trim Size (final size after being cut)
8.52" x 5.47"
216 x 139 mm
2556 x 1642 pixels
* Please be sure to keep all text within the safe margin.
Resolution
300 DPI

Target Market(s)

Adults in Northern California ages 30 - 80 that make the buying decisions for their families.

Industry/Entity Type

Pool Service

Font styles to use
Sans Serif

Colors
33a6d7
3277b5
acd037
fece3e

Requirements
Must have
• - company logo
- detail on variable speed pump
- cost savings chart
- image of family having fun (something related to the question on the front of the postcard - what would you do with $100/month?)

```html
<!DOCTYPE html>
<html lang="en">
<head>
<meta charset="utf-8">
<title>Keller &amp; Sons Pool Service – Variable Speed Pump Postcard</title>
<link rel="stylesheet" href="https://fonts.googleapis.com/css2?family=PT+Sans:ital,wght@0,400;0,700;1,700&family=PT+Sans+Narrow:wght@400;700&family=Kaushan+Script&family=Courgette&display=swap">
<style>
  :root {
    --navy: #2b2b7a;
    --navy-deep: #2e2a6e;
    --ocean: #3277b5;
    --sky: #33a6d7;
    --cyan: #1fb3e0;
    --lime: #acd037;
    --sun: #fece3e;
    --teal: #1aa7b0;
    --grey: #6a6a6a;
    --rule: #555555;
    --white: #ffffff;
  }
  * { margin: 0; padding: 0; box-sizing: border-box; }
  html, body { width: 1200px; height: 433px; overflow: hidden; background: var(--white); }
  body { position: relative; font-family: "PT Sans", Arial, sans-serif; }

  /* ---------- Front ---------- */
  .front {
    position: absolute; left: 0; top: 0; width: 605px; height: 433px;
    border: 1px solid var(--navy); background: var(--white); overflow: hidden;
  }
  .front__photo {
    position: absolute; left: 0; top: 0; width: 100%; height: 341px;
    background: radial-gradient(ellipse at 40% 40%, #a5d9cf 0%, #5cc3d6 40%, #1b9fc4 100%);
  }
  .front__headline {
    position: absolute; right: 16px; top: 244px; text-align: right;
    font-family: "Courgette", cursive; color: var(--white);
    text-shadow: 2px 2px 0 var(--navy); line-height: 1.05;
  }
  .front__headline .line1 { font-size: 29px; display: block; margin-right: 18px; }
  .front__headline .line2 { font-size: 29px; }
  .front__headline .amount { font-family: "PT Sans", sans-serif; font-weight: 700; font-size: 42px; }
  .front__headline .per { font-size: 16px; }
  .front__headline .q { font-size: 42px; }

  .front__offer {
    position: absolute; left: 15px; top: 359px; width: 285px;
    color: var(--navy); font-weight: 700; font-size: 15px; line-height: 21px;
  }
  .front__offer strong { font-style: italic; font-size: 19px; }

  .partner {
    position: absolute; display: flex; align-items: center; gap: 6px;
    color: var(--navy); font-weight: 700; line-height: 1;
  }
  .partner--brantley { left: 300px; top: 358px; font-size: 20px; }
  .partner--corvane { left: 298px; top: 393px; font-size: 23px; }
  .partner__mark { width: 16px; height: 16px; background: var(--navy); }
  .partner--corvane .partner__mark { background: var(--lime); width: 20px; height: 20px; }

  .badge { position: absolute; left: 460px; top: 356px; width: 122px; text-align: center; font-family: "PT Sans Narrow", sans-serif; line-height: 1.1; white-space: nowrap; }
  .badge__plate { width: 122px; height: 36px; background: var(--sky); }
  .badge__title { margin-top: 4px; font-size: 13px; font-weight: 700; color: var(--ocean); }
  .badge__sub { font-size: 13px; color: var(--ocean); }

  /* ---------- Back ---------- */
  .back { position: absolute; left: 615px; top: 0; width: 585px; height: 433px; background: var(--white); border: 1px solid #d8d8d8; }

  .brand { position: absolute; left: 14px; top: 28px; display: flex; align-items: center; gap: 6px; color: var(--navy); font-weight: 700; font-size: 22px; }
  .brand__mark { width: 14px; height: 14px; border-radius: 50%; background: var(--sky); }

  .address { position: absolute; left: 13px; top: 76px; color: var(--grey); font-size: 16.5px; line-height: 1.2; }

  .tagline { position: absolute; left: 16px; top: 126px; font-family: "Kaushan Script", cursive; line-height: 1.15; font-size: 17px; color: var(--teal); }
  .tagline .rank { color: var(--navy); font-size: 19px; display: block; }

  .savings { position: absolute; left: 0; top: 201px; width: 273px; height: 142px; display: flex; }
  .savings__chart { width: 123px; background: var(--ocean); color: var(--white); padding: 3px 5px 0; font-family: "PT Sans Narrow", sans-serif; overflow: hidden; }
  .savings__title { color: var(--sun); font-weight: 700; font-size: 13.5px; line-height: 1; }
  .savings__title small { font-size: 7.5px; font-weight: 400; color: var(--white); }
  .savings__stats { display: flex; gap: 7px; margin-top: 4px; font-weight: 700; font-size: 12px; line-height: 1; }
  .savings__stats small { display: block; font-size: 6px; font-weight: 400; }
  .savings__table { width: calc(100% + 10px); margin: 3px -5px 0; border-collapse: collapse; font-size: 12px; }
  .savings__table th { font-size: 6.5px; font-weight: 400; color: var(--sun); text-align: left; padding: 1px 2px; line-height: 1.05; }
  .savings__table td { padding: 1px 3px; font-weight: 700; line-height: 1; }
  .savings__table td.label { font-size: 6px; font-weight: 400; font-style: italic; width: 46px; line-height: 1; }
  .savings__table tr.band td, .savings__table tr.band th { background: var(--sky); }
  .savings__table tr.band-dark td { background: #2a5fa5; }

  .savings__offers { flex: 1; background: var(--cyan); color: var(--white); padding: 8px 5px 0 6px; font-family: "PT Sans Narrow", sans-serif; font-size: 10.5px; line-height: 1.12; list-style: none; }
  .savings__offers li { margin-bottom: 8px; padding-left: 6px; text-indent: -6px; }
  .savings__offers li::before { content: "· "; }

  .disclaimer { position: absolute; left: 0; top: 343px; width: 273px; height: 90px; background: var(--navy-deep); color: #e9e9f4; padding: 9px 12px; font-family: "Times New Roman", serif; font-size: 7.6px; line-height: 1.35; }

  .address-line { position: absolute; left: 309px; width: 242px; height: 0; border-top: 1px solid var(--rule); }
  .address-line--1 { top: 268px; }
  .address-line--2 { top: 303px; }
  .address-line--3 { top: 337px; }

  .contact { position: absolute; left: 309px; top: 359px; color: var(--navy); font-family: "PT Sans Narrow", sans-serif; font-size: 15.5px; line-height: 22px; }
</style>
</head>
<body>

<section class="front">
  <div class="front__photo" role="img" aria-label="Photo of a smiling family in snorkel masks floating together on a green raft in a bright blue pool"></div>
  <p class="front__headline">
    <span class="line1">What would you do with</span>
    <span class="line2">an extra <span class="amount">$100</span><span class="per">/Month</span><span class="q">?</span></span>
  </p>

  <p class="front__offer"><strong>Save $80 - $100</strong>/month (average)<br>on your energy bill by moving to a<br>variable speed pump.</p>

  <div class="partner partner--brantley"><span class="partner__mark"></span>BRANTLEY</div>
  <div class="partner partner--corvane"><span class="partner__mark"></span>Corvane</div>

  <div class="badge">
    <div class="badge__plate"></div>
    <p class="badge__title">PARTNER OF THE YEAR</p>
    <p class="badge__sub">Sustained Excellence</p>
  </div>
</section>

<section class="back">
  <div class="brand"><span class="brand__mark"></span>Keller &amp; Sons</div>
  <p class="address">2450 Harbor Lane, Suite 210<br>Fairbrook, CA 95600</p>

  <p class="tagline">Trust only the best to upgrade your pool equipment!
    <span class="rank">Keller &amp; Sons is Sacramento's #1</span>rated pool service and repair company.</p>

  <div class="savings">
    <div class="savings__chart">
      <p class="savings__title">Energy Savings<br>Example <small>(20,000 gallon pool)</small></p>
      <div class="savings__stats">
        <span>$147<small>per month</small></span>
        <span>$1,764<small>per season</small></span>
        <span>95%</span>
      </div>
      <table class="savings__table">
        <tr class="band"><th></th><th>Variable speed pump</th><th>Single speed pump</th></tr>
        <tr class="band-dark"><td class="label">Cost of operation per season</td><td>$84</td><td>$1,848</td></tr>
        <tr class="band"><td class="label">Run time per day (hours)</td><td>12</td><td>8</td></tr>
        <tr class="band-dark"><td class="label">Turnovers per day</td><td>1.0</td><td>2.1</td></tr>
      </table>
    </div>
    <ul class="savings__offers">
      <li>Contact us within 30 days of receiving this postcard to schedule your <b><i>Free Energy Audit</i></b>.</li>
      <li>Upgrade to a variable speed pump at $1000 or more &amp; receive 1-month of pool cleaning service <b><i>FREE!</i></b></li>
      <li>Payment options are available.</li>
    </ul>
  </div>

  <p class="disclaimer">Calculated energy savings are based on the selected speed only and System Curve C per California's Title 20 Appliance Energy Regulations. Operation at additional speeds may be required when using other equipment such as heaters, water features, etc. Actual savings may vary based on the single speed pump model and other hydraulic aspects such as plumbing size and length.</p>

  <span class="address-line address-line--1"></span>
  <span class="address-line address-line--2"></span>
  <span class="address-line address-line--3"></span>

  <p class="contact">Call today! 916-555-0148<br>w: www.keller-sons.com<br>e: hello@keller-sons.com</p>
</section>

</body>
</html>
```